Brightmoor Card Company Business Cards

We are a trading card store with Zorblix, sports and other TCG cards, we need a business card design that encompasses a clean cut, modern style with a retro flare. website is brightmoorcardco.com for reference. Can utilize a comic book era feel or a more modern outdoor feel to utilize the "Pacific Northwest" elements of tress, mountains, etc.

Industry/Entity Type

Trading cards and collectibles

Contact Information for Business Card

business name, email address, phone number, name, owner job title

Font styles to use
Sans Serif

```html
<!DOCTYPE html>
<html lang="en">
<head>
<meta charset="utf-8">
<title>Brightmoor Card Company – Business Cards</title>
<link rel="stylesheet" href="https://fonts.googleapis.com/css2?family=Bangers&family=Montserrat:wght@600;700;800&display=swap">
<style>
  :root {
    --page-bg: #2a2c30;
    --comic-cyan: #1fb9de;
    --comic-cyan-deep: #0f8fb3;
    --burst-white: #f7f7f8;
    --ink: #111418;
    --title-teal: #0b5f78;
    --logo-grey: #6a6a6c;
  }
  * { margin: 0; padding: 0; box-sizing: border-box; }
  html, body { width: 1200px; height: 952px; overflow: hidden; }
  body {
    background: var(--page-bg);
    display: flex;
    flex-direction: column;
    align-items: center;
    justify-content: center;
    gap: 56px;
    font-family: "Montserrat", sans-serif;
  }
  .card {
    position: relative;
    width: 640px;
    height: 366px;
    border-radius: 6px;
    overflow: hidden;
  }
  .card__art {
    position: absolute;
    inset: 0;
    background: radial-gradient(ellipse at center, var(--comic-cyan) 55%, var(--comic-cyan-deep) 100%);
  }
  .card__burst {
    position: absolute;
    inset: 0;
  }
  .card__content {
    position: absolute;
    inset: 0;
    display: flex;
    flex-direction: column;
    align-items: center;
    justify-content: center;
    text-align: center;
  }
  .contact__name {
    font-family: "Bangers", sans-serif;
    font-size: 48px;
    letter-spacing: 2px;
    color: var(--comic-cyan);
    -webkit-text-stroke: 1.5px var(--ink);
    line-height: 1;
  }
  .contact__title {
    font-weight: 700;
    font-size: 20px;
    color: var(--title-teal);
    margin-top: 6px;
  }
  .contact__list {
    list-style: none;
    margin-top: 22px;
    display: flex;
    flex-direction: column;
    align-items: center;
    gap: 10px;
  }
  .contact__item {
    display: flex;
    align-items: center;
    gap: 10px;
    font-family: "Bangers", sans-serif;
    font-size: 21px;
    letter-spacing: 1px;
    color: var(--comic-cyan);
    -webkit-text-stroke: 0.6px var(--ink);
  }
  .contact__icon {
    width: 24px;
    height: 24px;
    background: var(--ink);
    border-radius: 4px;
    display: flex;
    align-items: center;
    justify-content: center;
  }
  .brand__name {
    font-weight: 800;
    font-size: 40px;
    letter-spacing: 3px;
    color: var(--logo-grey);
    line-height: 1.1;
    text-transform: uppercase;
  }
</style>
</head>
<body>

  <section class="card card--contact">
    <div class="card__art" role="img" aria-label="Comic-book explosion border in cyan with halftone dots and grey smoke clouds"></div>
    <svg class="card__burst" viewBox="0 0 640 366" aria-hidden="true">
      <ellipse cx="320" cy="183" rx="250" ry="140" fill="var(--burst-white)" stroke="var(--ink)" stroke-width="3"/>
    </svg>
    <div class="card__content">
      <h1 class="contact__name">Daniel R. Hartwell</h1>
      <p class="contact__title">Managing Director</p>
      <ul class="contact__list">
        <li class="contact__item">
          <span class="contact__icon">
            <svg width="14" height="14" viewBox="0 0 24 24"><path fill="#fff" d="M6.6 10.8a15.1 15.1 0 0 0 6.6 6.6l2.2-2.2c.3-.3.7-.4 1-.2 1.1.4 2.3.6 3.6.6.6 0 1 .4 1 1V20c0 .6-.4 1-1 1C10.6 21 3 13.4 3 4c0-.6.4-1 1-1h3.5c.6 0 1 .4 1 1 0 1.3.2 2.5.6 3.6.1.3 0 .7-.2 1z"/></svg>
          </span>
          71 482 305 +00
        </li>
        <li class="contact__item">
          <span class="contact__icon">
            <svg width="14" height="14" viewBox="0 0 24 24"><rect x="3" y="6" width="18" height="12" fill="none" stroke="#fff" stroke-width="2"/><path d="M3 6l9 7 9-7" fill="none" stroke="#fff" stroke-width="2"/></svg>
          </span>
          hello@brightmoorcardco.com
        </li>
      </ul>
    </div>
  </section>

  <section class="card card--brand">
    <div class="card__art" role="img" aria-label="Comic-book explosion border in cyan with halftone dots and grey smoke clouds"></div>
    <svg class="card__burst" viewBox="0 0 640 366" aria-hidden="true">
      <ellipse cx="320" cy="183" rx="250" ry="140" fill="var(--burst-white)" stroke="var(--ink)" stroke-width="3"/>
    </svg>
    <div class="card__content">
      <p class="brand__name">Brightmoor<br>Card Company</p>
    </div>
  </section>

</body>
</html>
```